Watch brand needs new business cards

Fernhollow Clock Company are looking for a new business card design incorporating our logo and brand colours as per our website.

Design should be 90x55mm with 3mm print margin from edges and 3mm external bleed.

Card should be double sided, e.g. logo one side, personal details on the other.

Logo will be provided as a vector.

The card must be able to show:
- Staff name
- Position
- Office Address
- Email
- Telephone number
- Website address

Final work must be provided in an editable format to allow us to add staff details (e.g. an AI or PSD file).

Industry/Entity Type

Business

```html
<!DOCTYPE html>
<html lang="en">
<head>
<meta charset="utf-8">
<title>Fernhollow Clock Company – Business Cards</title>
<link rel="stylesheet" href="https://fonts.googleapis.com/css2?family=Open+Sans:wght@400;600&display=swap">
<style>
  :root {
    --backdrop: #ece9e4;
    --kraft-light: #cfb084;
    --kraft-mid: #c4a375;
    --kraft-dark: #b39066;
    --ink: #1f1a14;
    --ink-faint: rgba(120, 92, 60, 0.22);
  }
  * { margin: 0; padding: 0; box-sizing: border-box; }
  html, body {
    width: 1200px;
    height: 900px;
    overflow: hidden;
    background: var(--backdrop);
  }
  .canvas {
    position: relative;
    width: 1200px;
    height: 900px;
  }
  .card {
    position: absolute;
    height: 342px;
    background: radial-gradient(ellipse at 45% 35%, var(--kraft-light) 0%, var(--kraft-mid) 60%, var(--kraft-dark) 100%);
    box-shadow: 0 6px 18px rgba(0, 0, 0, 0.18);
    font-family: "Open Sans", sans-serif;
    color: var(--ink);
  }
  .card--details { left: 238px; top: 62px; width: 555px; }
  .card--brand { left: 458px; top: 518px; width: 559px; }

  .details-ring {
    position: absolute;
    left: 84px; top: 0;
    width: 386px; height: 342px;
  }

  .details {
    position: absolute;
    left: 0; right: 0;
    top: 86px;
    text-align: center;
  }
  .details__name { font-size: 18px; font-weight: 600; line-height: 26px; }
  .details__position { font-size: 14px; line-height: 18px; margin-bottom: 13px; }
  .details__line { font-size: 14px; line-height: 20px; }
  .details__gap { height: 15px; }

  .brand-mark {
    position: absolute;
    left: 50%; top: 96px;
    width: 86px; height: 86px;
    margin-left: -43px;
  }
  .brand-name {
    position: absolute;
    left: 0; right: 0;
    top: 196px;
    text-align: center;
    font-size: 30px;
    font-weight: 600;
    letter-spacing: 0.5px;
    color: var(--ink);
  }
</style>
</head>
<body>
  <main class="canvas">
    <section class="card card--details" aria-label="Card back: staff details">
      <svg class="details-ring" viewBox="0 0 386 342" aria-hidden="true">
        <circle cx="193" cy="171" r="188" fill="none" stroke="var(--ink-faint)" stroke-width="10"/>
      </svg>
      <div class="details">
        <p class="details__name">Elias Marlow</p>
        <p class="details__position">Position</p>
        <p class="details__line">48 Linden Row, Harbourside</p>
        <p class="details__line">Southvale, 402613.</p>
        <div class="details__gap"></div>
        <p class="details__line">055-281 730 416</p>
        <p class="details__line">info@fernhollowclock.example</p>
        <p class="details__line">www.fernhollowclock.example</p>
      </div>
    </section>

    <section class="card card--brand" aria-label="Card front: company name">
      <svg class="brand-mark" viewBox="0 0 86 86" aria-hidden="true">
        <circle cx="43" cy="43" r="40" fill="none" stroke="var(--ink)" stroke-width="4"/>
      </svg>
      <p class="brand-name">Fernhollow Clock Company</p>
    </section>
  </main>
</body>
</html>
```